Home Inspection Postcard Design

Home inspection. Attached is my old postcard. I would like the card to have the same verbage on it - front and back. but I would like the house graphic and the colors to be blues. The only changes to the information is the website address is www.brightoakhps.com. THe PO Box is now 381 rather than 647, and I wanted to add my email address which is brightoakhps@quillmail.net. I would like to keep the $25 off box but add "or a 10% military discount, which ever is greater" or something like that .If you could mock something up for me I would really appreciate it. I would also like a glossy finish on the cards

Home Inspection

```html
<!DOCTYPE html>
<html lang="en">
<head>
<meta charset="utf-8">
<title>Bright Oak Home Inspection Services – Postcard</title>
<link rel="stylesheet" href="https://fonts.googleapis.com/css2?family=Titillium+Web:wght@400;600;700&family=Open+Sans:ital,wght@0,400;0,600;1,400&family=Indie+Flower&display=swap">
<style>
  :root {
    --brand-blue: #2271b9;
    --brand-blue-dark: #1a5c9c;
    --ink: #2e2e2e;
    --paper: #ffffff;
    --backdrop: #2b2b2b;
    --rule: #9a9a9a;
    --sky-top: #cfe3f3;
    --sky-low: #eef4f8;
    --stucco: #e7d2b8;
    --lawn: #8cae6a;
    --siding: #5d88ad;
  }
  * { box-sizing: border-box; margin: 0; padding: 0; }
  html, body { width: 1200px; height: 1110px; overflow: hidden; }
  body { background: var(--backdrop); font-family: "Open Sans", sans-serif; color: var(--ink); position: relative; }

  .card { position: absolute; background: var(--paper); }
  .card-front { left: 90px; top: 32px; width: 667px; height: 517px; }
  .card-back { left: 425px; top: 571px; width: 661px; height: 515px; }

  .brand { position: absolute; display: flex; align-items: flex-start; gap: 8px; }
  .brand-dot { width: 20px; height: 20px; border-radius: 50%; background: var(--brand-blue); margin-top: 6px; flex: none; }
  .brand-name { font-family: "Titillium Web", sans-serif; color: var(--brand-blue); font-weight: 700; line-height: 1.05; }
  .brand-name .line1 { display: block; font-size: 19px; }
  .brand-name .line2 { display: block; font-size: 14.5px; }

  .front-brand { left: 96px; top: 22px; }

  .photo-strip { position: absolute; background: linear-gradient(180deg, var(--sky-top) 0%, var(--stucco) 45%, #d9bd9b 70%, var(--lawn) 100%); }
  .strip-1 { left: 24px; top: 102px; width: 76px; height: 203px; }
  .strip-2 { left: 108px; top: 79px; width: 77px; height: 218px; }
  .strip-3 { left: 192px; top: 79px; width: 76px; height: 233px; }
  .strip-4 { left: 277px; top: 71px; width: 76px; height: 224px; }
  .strip-5 { left: 361px; top: 59px; width: 75px; height: 233px; }

  .motto-box { position: absolute; left: 25px; top: 323px; width: 410px; height: 65px; background: var(--brand-blue); color: #fff; text-align: center; }
  .motto { font-family: "Indie Flower", cursive; font-size: 21px; letter-spacing: 0.5px; margin-top: 6px; line-height: 28px; }
  .credentials { font-size: 14.5px; line-height: 22px; }

  .front-intro { position: absolute; left: 26px; top: 398px; width: 410px; font-size: 13.3px; line-height: 17.6px; text-align: justify; }

  .divider { position: absolute; left: 452px; top: 9px; width: 2px; height: 468px; background: repeating-linear-gradient(180deg, var(--brand-blue) 0 34px, transparent 34px 42px); }

  .offer-badge { position: absolute; left: 490px; top: 26px; width: 136px; height: 136px; }
  .offer-note { position: absolute; left: 470px; top: 168px; width: 177px; text-align: center; font-style: italic; font-size: 14px; }
  .front-pitch { position: absolute; left: 470px; top: 207px; width: 177px; font-size: 13.3px; line-height: 17.9px; text-align: justify; hyphens: auto; }

  .web-bar { position: absolute; height: 29px; background: var(--brand-blue); color: #fff; font-family: "Titillium Web", sans-serif; font-weight: 600; font-size: 14px; letter-spacing: 9px; text-align: center; line-height: 29px; }
  .card-front .web-bar { left: 10px; top: 478px; width: 649px; }
  .card-back .web-bar { left: 11px; top: 477px; width: 647px; }

  .back-photo { position: absolute; left: 11px; top: 10px; width: 364px; height: 226px; background: linear-gradient(180deg, var(--sky-low) 0%, #dce8f0 30%, var(--siding) 55%, #4f7a9e 78%, var(--lawn) 100%); }
  .back-brand { left: 26px; top: 16px; }

  .question-band { position: absolute; left: 375px; top: 10px; width: 26px; height: 465px; background: var(--brand-blue); }
  .question-band span { position: absolute; left: 50%; top: 120px; transform: translateX(-50%) rotate(90deg); transform-origin: center; white-space: nowrap; color: #fff; font-family: "Titillium Web", sans-serif; font-weight: 700; font-size: 13.5px; letter-spacing: 0.3px; display: block; width: 230px; margin-left: 0; text-align: center; }

  .back-copy { position: absolute; left: 17px; top: 248px; width: 347px; font-size: 12.2px; line-height: 15.75px; text-align: justify; }

  .stamp-box { position: absolute; left: 543px; top: 35px; width: 93px; height: 88px; border: 1px solid var(--rule); }
  .address-line { position: absolute; left: 417px; width: 219px; height: 1px; background: var(--rule); }
  .line-a { top: 190px; } .line-b { top: 233px; } .line-c { top: 279px; }

  .return-address { position: absolute; left: 463px; top: 382px; font-family: "Titillium Web", sans-serif; font-weight: 700; color: var(--brand-blue); font-size: 14.5px; line-height: 18px; }
  .mail-icon { position: absolute; left: 412px; top: 413px; width: 40px; height: 40px; }
  .return-email { position: absolute; left: 463px; top: 434px; font-family: "Titillium Web", sans-serif; font-weight: 700; color: var(--brand-blue); font-size: 14.5px; }
</style>
</head>
<body>

<section class="card card-front">
  <div class="brand front-brand">
    <span class="brand-dot"></span>
    <span class="brand-name"><span class="line1">BRIGHT OAK</span><span class="line2">Home Inspection Services LLC</span></span>
  </div>

  <div role="img" aria-label="Photograph of a large stucco house with tiled roof and garage, shown in five vertical strips">
    <div class="photo-strip strip-1"></div>
    <div class="photo-strip strip-2"></div>
    <div class="photo-strip strip-3"></div>
    <div class="photo-strip strip-4"></div>
    <div class="photo-strip strip-5"></div>
  </div>

  <div class="motto-box">
    <p class="motto">“ We Leave No Stone Unturned “</p>
    <p class="credentials">Licensed, Certified &amp; insured</p>
  </div>

  <p class="front-intro">Enjoy the comfort of peace-of-mind before buying your new home. Our trained professionals inspect the property and immediately present you with a detailed. yet clear report. They will answer any questions you may have.</p>

  <div class="divider"></div>

  <svg class="offer-badge" viewBox="0 0 136 136" aria-label="25% off services">
    <polygon fill="#2271b9" points="68,0 74.2,14.8 84.8,2.8 87.1,18.8 100.4,9.6 98.6,25.6 113.8,20 107.9,35 124,34 114.2,46.8 129.8,51 117.3,61 131.5,68.9 116.8,75.8 128.9,86.8 113,90.4 120.4,104.7 104.5,104 107.3,119.8 92.5,113.8 90.3,129.8 78.5,119 72.2,134 65.4,119.4 55,131.6 52.7,115.7 39.4,124.9 41.2,108.9 26,114.5 31.9,99.5 15.8,100.5 25.6,87.7 10,83.5 22.5,73.5 8.3,65.6 23,58.7 10.9,47.7 26.8,44.1 19.4,29.8 35.3,30.5 32.5,14.7 47.3,20.7 49.5,4.7 61.3,15.5"/>
    <g transform="rotate(-20 68 68)" fill="#fff" font-family="Titillium Web, sans-serif" font-weight="700" text-anchor="middle">
      <text x="68" y="64" font-size="17">25% OFF</text>
      <text x="68" y="84" font-size="17">Services</text>
    </g>
  </svg>

  <p class="offer-note">with this postcard</p>

  <p class="front-pitch">Join our experienced in&shy;spectors in their tour of the property. They will acquaint you with its strengths and weknesses. You will feel confident in their judge&shy;ment and thoroughness. Many Realtors, Sellers, Home Buyers, Mortgage Companies and relocation companies have used our comprehensive report and services to their satisfac&shy;tion.</p>

  <div class="web-bar">www.brightoakhps.com</div>
</section>

<section class="card card-back">
  <div class="back-photo" role="img" aria-label="Photograph of a blue two-storey clapboard house with gables and a front porch on a lawn"></div>
  <div class="brand back-brand">
    <span class="brand-dot"></span>
    <span class="brand-name"><span class="line1">BRIGHT OAK</span><span class="line2">Home Inspection Services LLC</span></span>
  </div>

  <div class="question-band"><span>WHY DO I NEED AN INSPECTION?</span></div>

  <p class="back-copy">The purchase of a home or commercial building is one of the largest single investments you will ever make. You should know what to expect - in terms of needed and possible repairs and maintenance. A fresh coat of paint could be hiding serious problems. Stains on the ceiling may indicate a chronic roof leak or may be simply the result of a single incident. The inspector reviews these and other clues, then presents a professional opinion as to the condition of the property to help you avoid unpleasant seuprises afterward. Of course, an inspection may also point out the positive aspects of a building, as well as the type of maintenance needed to keep it in proper shape. After the inspection, you will have a much clearer understanding of the property and be able to make your purchasing decision confidently.</p>

  <div class="stamp-box"></div>
  <div class="address-line line-a"></div>
  <div class="address-line line-b"></div>
  <div class="address-line line-c"></div>

  <p class="return-address">PO Box 381<br>Harlow, GA 30417</p>
  <svg class="mail-icon" viewBox="0 0 40 40" aria-hidden="true">
    <circle cx="20" cy="20" r="18" fill="none" stroke="#2271b9" stroke-width="3"/>
    <rect x="10" y="13" width="20" height="14" rx="1.5" fill="#2271b9"/>
    <polyline points="10.5,14 20,21.5 29.5,14" fill="none" stroke="#fff" stroke-width="1.6"/>
  </svg>
  <p class="return-email">brightoakhps@quillmail.net</p>

  <div class="web-bar">www.brightoakhps.com</div>
</section>

</body>
</html>
```